Industrial Automation company requires a business card design

Valtrin Automation provides design & build of Automated Equipment for manufacturing industry.
www.valtrinautomation.example
The equipment we design is used for manufacturing in sectors such as medical device, pharmaceutical, aerospace and electronics.
We require a new business card design which incorporates our (New) logo and the key message words:
Automated Equipment:
Design, Build, Control, Test, Support

```html
<!DOCTYPE html>
<html lang="en">
<head>
<meta charset="utf-8">
<title>Valtrin Automation – Business Card</title>
<link rel="stylesheet" href="https://fonts.googleapis.com/css2?family=Roboto:wght@400;500;700&display=swap">
<style>
  :root {
    --backdrop: #3b3c3f;
    --card-white: #ffffff;
    --card-black: #1c1c1d;
    --brand-green: #1f8a3e;
    --ink-dark: #2a2a2a;
    --ink-grey: #5a5a5a;
    --ink-light: #f2f2f2;
  }
  * { box-sizing: border-box; margin: 0; padding: 0; }
  html, body {
    width: 1200px;
    height: 950px;
    overflow: hidden;
  }
  body {
    background: var(--backdrop);
    font-family: "Roboto", Arial, sans-serif;
    position: relative;
  }
  .card {
    position: absolute;
    left: 300px;
    width: 600px;
    height: 343px;
    border-radius: 4px;
    box-shadow: 0 10px 28px rgba(0,0,0,0.45);
  }

  /* Front */
  .card-front {
    top: 85px;
    background: var(--card-white);
    display: flex;
    flex-direction: column;
    align-items: center;
    justify-content: center;
    gap: 26px;
  }
  .wordmark {
    display: flex;
    align-items: center;
    gap: 14px;
  }
  .wordmark-square {
    width: 22px;
    height: 22px;
    background: var(--brand-green);
  }
  .wordmark-name {
    color: var(--brand-green);
    font-weight: 700;
    font-size: 38px;
    letter-spacing: 1px;
    text-transform: uppercase;
  }
  .key-message { text-align: center; }
  .key-message-title {
    color: var(--brand-green);
    font-weight: 500;
    font-size: 21px;
    margin-bottom: 6px;
  }
  .key-message-list {
    list-style: none;
    display: flex;
    gap: 8px;
    color: var(--ink-grey);
    font-size: 17px;
  }
  .key-message-list li + li::before {
    content: "\2022";
    color: var(--brand-green);
    margin-right: 8px;
  }

  /* Back */
  .card-back {
    top: 512px;
    background: linear-gradient(135deg, #2a2a2b 0%, var(--card-black) 55%, #121212 100%);
    padding: 56px 60px;
    display: flex;
    gap: 44px;
  }
  .back-mark {
    display: flex;
    flex-direction: column;
    align-items: flex-start;
    gap: 10px;
    width: 110px;
  }
  .back-mark-square {
    width: 74px;
    height: 74px;
    background: var(--brand-green);
  }
  .back-mark-name {
    color: var(--brand-green);
    font-weight: 700;
    font-size: 13px;
    text-transform: uppercase;
    line-height: 1.3;
  }
  .contact { color: var(--ink-light); }
  .contact-name {
    color: var(--brand-green);
    font-weight: 500;
    font-size: 22px;
  }
  .contact-role {
    font-size: 15px;
    margin-bottom: 22px;
  }
  .contact-address {
    font-style: normal;
    font-size: 15px;
    line-height: 1.35;
    margin-bottom: 20px;
  }
  .contact-lines {
    list-style: none;
    font-size: 15px;
    line-height: 1.55;
  }
  .contact-label {
    color: var(--brand-green);
    font-weight: 500;
  }
</style>
</head>
<body>
  <section class="card card-front">
    <div class="wordmark">
      <span class="wordmark-square"></span>
      <span class="wordmark-name">Valtrin Automation</span>
    </div>
    <div class="key-message">
      <p class="key-message-title">Automated Equipment</p>
      <ul class="key-message-list">
        <li>Design</li><li>Build</li><li>Control</li><li>Test</li><li>Support</li>
      </ul>
    </div>
  </section>

  <section class="card card-back">
    <div class="back-mark">
      <span class="back-mark-square"></span>
      <span class="back-mark-name">Valtrin Automation</span>
    </div>
    <div class="contact">
      <p class="contact-name">Marten Hale</p>
      <p class="contact-role">President</p>
      <address class="contact-address">2170 Quarry Lane<br>Elmsford Bay, NY 10599</address>
      <ul class="contact-lines">
        <li><span class="contact-label">Phone:</span> 555 0147 2290</li>
        <li><span class="contact-label">Fax:</span> 555 0183 6412</li>
        <li><span class="contact-label">Email:</span> marten@valtrinautomation.example</li>
        <li><span class="contact-label">Web:</span> www.valtrinautomation.example</li>
      </ul>
    </div>
  </section>
</body>
</html>
```